Robotic Physical Therapy office needs a Grand Opening Flyer

We need a Grand Opening flyer design for a robotic physical therapy office named Stellar Motion Therapy. We would like it to have a clean, classy, upscale feeling that gives potential clients a V.I.P. feeling. We would like to use the colors black, gray, and yellow (logo will be uploaded).

Event: Thursday, June 1st, 2023 from 12pm-6pm
location: 58274 Harlow Ave, Bloomfield Hills, MI 48319

Industry/Entity Type

Physical therapy

Font styles to use
Script

Colors

Designer to choose colors to be used in the design.

Requirements
Nice to have
• More of a vip feel for the invite

```html
<!DOCTYPE html>
<html lang="en">
<head>
<meta charset="utf-8">
<title>Stellar Motion Therapy – Grand Opening</title>
<link href="https://fonts.googleapis.com/css2?family=Poppins:wght@300;400;500;600;700&display=swap" rel="stylesheet">
<style>
  :root {
    --charcoal: #3a3a40;
    --yellow: #f9dc16;
    --white: #ffffff;
    --rule: #8a8a8f;
    --photo-light: #eceae6;
    --photo-mid: #b9b3ab;
    --photo-dark: #55555a;
  }
  html, body { margin: 0; padding: 0; overflow: hidden; background: #ffffff; }
  .flyer {
    position: relative;
    width: 848px;
    height: 1200px;
    overflow: hidden;
    background: var(--white);
    font-family: 'Poppins', sans-serif;
  }
  .photo-area {
    position: absolute;
    left: 0; top: 0;
    width: 560px; height: 1200px;
    background: linear-gradient(170deg, var(--photo-light) 0%, var(--photo-light) 25%, var(--photo-mid) 55%, var(--photo-dark) 100%);
  }
  .dark-panel { position: absolute; inset: 0; width: 848px; height: 1200px; }
  .brand {
    position: absolute;
    left: 30px; top: 40px;
    display: flex; align-items: center; gap: 14px;
  }
  .brand-dot {
    width: 62px; height: 62px; border-radius: 50%;
    background: var(--charcoal);
    flex: none;
  }
  .brand-name {
    margin: 0;
    font-size: 32px; line-height: 1.05; font-weight: 600;
    color: var(--charcoal);
    text-transform: uppercase;
  }
  .top-rule {
    position: absolute; left: 477px; top: 53px;
    width: 318px; height: 3px; background: var(--rule);
  }
  .accent { position: absolute; }
  .accent-small-top { left: 412px; top: 30px; width: 44px; height: 44px; border-radius: 50%; background: var(--yellow); }
  .accent-small-side { left: 332px; top: 144px; width: 34px; height: 34px; border-radius: 50%; background: var(--yellow); }
  .accent-marker { left: 418px; top: 134px; width: 12px; height: 88px; background: var(--white); opacity: 0.85; }
  .accent-photo { left: 36px; top: 748px; width: 116px; height: 88px; background: var(--yellow); opacity: 0.9; }
  .accent-large { left: 328px; top: 855px; width: 168px; height: 168px; border-radius: 50%; background: var(--yellow); }
  .accent-stem { left: 404px; top: 1032px; width: 20px; height: 152px; background: linear-gradient(180deg, var(--yellow), rgba(249,220,22,0.6)); }
  .headline {
    position: absolute; right: 53px; top: 112px;
    margin: 0; text-align: right;
    color: var(--yellow); font-weight: 700;
    font-size: 82px; line-height: 108px; letter-spacing: 1px;
  }
  .event-time {
    position: absolute; right: 53px; top: 338px;
    margin: 0; text-align: right;
    color: var(--white); font-weight: 500;
    font-size: 45px; line-height: 62px;
  }
  .address {
    position: absolute; right: 56px; top: 604px;
    margin: 0; text-align: right; font-style: normal;
    color: var(--white); font-weight: 300;
    font-size: 39px; line-height: 56px;
  }
  .contact {
    position: absolute; right: 60px; top: 903px;
    text-align: right; color: var(--white);
  }
  .contact .phone { margin: 0; font-size: 26px; line-height: 36px; font-weight: 400; }
  .contact .web { margin: 8px 0 0; font-size: 17px; font-weight: 400; }
  .social {
    position: absolute; left: 616px; top: 1020px;
    display: flex; gap: 16px;
  }
  .social span {
    width: 31px; height: 31px; border-radius: 50%;
    background: var(--white);
  }
  .corner-field {
    position: absolute; left: 612px; top: 1110px;
    width: 166px; height: 90px;
    background: linear-gradient(180deg, rgba(255,255,255,0.35), rgba(255,255,255,0.55));
    clip-path: polygon(50% 0, 100% 100%, 0 100%);
  }
</style>
</head>
<body>
<div class="flyer">
  <div class="photo-area" role="img" aria-label="Photo of a patient seated in a robotic physical therapy arm device, assisted by a therapist"></div>

  <svg class="dark-panel" viewBox="0 0 848 1200" aria-hidden="true">
    <polygon points="428,0 848,0 848,1200 372,1200 372,660 292,306" fill="var(--charcoal)"/>
  </svg>

  <div class="brand">
    <span class="brand-dot"></span>
    <p class="brand-name">Stellar Motion<br>Therapy</p>
  </div>

  <div class="top-rule"></div>

  <div class="accent accent-small-top" role="img" aria-label="Small yellow decorative accent"></div>
  <div class="accent accent-small-side" role="img" aria-label="Small yellow decorative accent"></div>
  <div class="accent accent-marker" role="img" aria-label="White decorative accent"></div>
  <div class="accent accent-photo" role="img" aria-label="Yellow decorative accent"></div>

  <h1 class="headline">GRAND<br>OPENING</h1>

  <p class="event-time">THURSDAY<br>JUNE 1st, 2023<br>12PM-6PM</p>

  <address class="address">58274<br>Harlow Ave,<br>Bloomfield Hills,<br>MI 48319</address>

  <div class="accent accent-large" role="img" aria-label="Large yellow decorative accent"></div>
  <div class="accent accent-stem" role="img" aria-label="Yellow decorative accent"></div>

  <div class="contact">
    <p class="phone">+30 555 018 274</p>
    <p class="phone">+30 555 018 274</p>
    <p class="web">www.stellarmotion.com</p>
  </div>

  <div class="social" aria-label="Social media">
    <span></span><span></span><span></span><span></span>
  </div>

  <div class="corner-field" role="img" aria-label="Soft white decorative accent"></div>
</div>
</body>
</html>
```